Event Listing Website

We need a redesign of a site for a new startup that lists local events such as concerts, night clubs, stand up comedy shows, theater plays, festivals, conferences, seminars, and family events.

The original design was done by programmers, not designers, and thus can be greatly improved, especially in terms of flow and usability.

The current site can be viewed at:
http://projects.brinvexsystems.example/pellora/index.php/events/

The successful designer may also be hired for additional work. In fact, we are looking for a long-time partner that may eventually fill a Creative Director role with this new venture..

Things to note:

The site should not look like a nightlife/disco/club site since the site lists events from concerts to conferences to family events.

There is a lot of content on the site, thus it needs to be clean, easy to read and navigate.

Our mission is to have a “Unique” site, that stands out from the traditional ones

Currently the site has these main sections:

Homepage
Events
Venues
Cinema

These sections have the following content types or page layouts:

Homepage
Listing of events
Listing of venues
Event details
Venue details
Cinema summary page
Film details
Film theater details
Blog/news
Account overview page
Updates

Please note, an important element of the site is the location picker that is currently on the top left of our site (the black drop down button that says "change", enter Roma for example). The site displays events based on user location, users need to know what city the site is using and need to be able to change such city. This works similar to many sites such as www.dealnorva.example, www.partyvesk.example, and www.happenlo.example.

Also, please note that we would eventually use background ads on the homepage. See www.ticketmurn.example for example.

I have extended the project further. Thanks!

Please note, after the main menu (Home, Events, Venues, Cinema) these pages or features are very important and should be visible and prominent. We currently have them on a bar across the top that remains fixed as you scroll down, but it may not be the best location, so we look forward to some fresh ideas. Thanks.

In order of importance:

1. Change your location (Button that says current city with option to change it)
2. Add event (link)
3. Add venue (link)
4. Login (link)
5. Change language (drop down button with languages)

I just increased the budget by $40 :)

When submitting a design, please submit two versions, one with background advertisement, and one without. This way we can see if there are too many colors or distractions.

Here is a sample background advertisement to use: http://lentobanner.example/img_uploads/72/77_191072_3_Korvex_Viola_Tab_Adriva_newsln_skin2.jpg

Hello all, thanks for submitting your beautiful designs. It has made our decision very difficult. We decided to award to project to Merostin, who is currently working on making some tweaks to his submission. Thus are no longer accepting designs. Thanks again.

Target Market(s)

17-40 year olds, male and female, clubbers, concert goers, professionals, athletes, families, and kids

Industry/Entity Type

Events

Requirements
Must have
• Needs to follow 960 grid system. See http://gridlane.example.
Nice to have
• We like the colors Bravik Nearby
(http://nearby.bravik.example/westside-south-bay)

We like Dealnorva theme as well
(http://www.dealnorva.example/los-angeles/)

Happenlo is a site similar to ours, we like the overall layout and how easy it is to navigate, not necessarily the colors though:
(http://happenlo.example/)
Should not have
• The site should not look like a nightlife/disco/club site.

Besides clubs, the site lists events from concerts to conferences to family events.

Should definitely not use serif fonts such as Times New Roman

```html
<!DOCTYPE html>
<html lang="en">
<head>
<meta charset="utf-8">
<title>Pellora – Events in Roma</title>
<link rel="stylesheet" href="https://fonts.googleapis.com/css2?family=Arimo:wght@400;700&display=swap">
<style>
:root{
  --page:#ebebea;
  --blue:#0aa6dc;
  --blue-dark:#0a8fc4;
  --orange:#e2560d;
  --green:#7fd321;
  --green-dark:#5aab12;
  --ink:#333;
  --muted:#777;
  --line:#dadada;
  --panel:#fff;
  --band:#4a4a4a;
  --footer:#1f1f1f;
  --footer-text:#8a8a8a;
}
*{box-sizing:border-box;margin:0;padding:0}
html,body{width:668px;height:1200px;overflow:hidden}
body{background:var(--page);font-family:"Arimo",Arial,sans-serif;color:var(--ink);position:relative;font-size:9px}
.abs{position:absolute}
a{color:inherit;text-decoration:none}

/* header */
.topbar{left:72px;top:44px;width:524px;height:39px;background:var(--blue);color:#fff}
.brand{position:absolute;left:10px;top:7px;font-size:21px;font-weight:400;letter-spacing:.3px}
.mainnav{position:absolute;left:123px;top:0;display:flex;height:39px}
.mainnav a{width:45px;display:flex;flex-direction:column;align-items:center;justify-content:flex-end;padding-bottom:4px;font-size:10px;font-weight:700;gap:3px}
.mainnav a.current{background:var(--orange)}
.mainnav svg{width:13px;height:13px}
.search{position:absolute;right:10px;top:13px;width:110px;height:14px;border:1px solid #fff;background:var(--blue-dark);font-size:8px;padding:2px 4px;color:#dff}
.search svg{position:absolute;right:3px;top:2px;width:9px;height:9px}
.subbar{left:72px;top:83px;width:524px;height:25px;background:var(--blue-dark);color:#fff;font-size:10px}
.subbar > *{position:absolute;top:6px;white-space:nowrap}
.city b{background:var(--orange);padding:1px 4px;font-weight:700}
.plus{display:inline-block;width:10px;height:10px;background:var(--orange);color:#fff;text-align:center;line-height:10px;font-size:9px;font-weight:700;margin-left:3px;font-style:normal}
.subbar .lang{background:#2a6d99;padding:2px 6px;top:5px}

/* hero */
.slider{left:83px;top:126px;width:335px;height:171px;background:radial-gradient(circle at 45% 45%,#f3a12a,#b45a0a 45%,#3a1a05 85%)}
.arrow{position:absolute;top:66px;width:20px;height:20px;background:var(--green);display:flex;align-items:center;justify-content:center}
.caption{position:absolute;left:0;bottom:0;width:100%;height:40px;background:rgba(0,0,0,.45);color:#fff;padding:6px 6px}
.caption h2{font-size:14px;font-weight:700}
.caption p{font-size:9px;margin-top:2px}
.dots{position:absolute;right:12px;bottom:14px;display:flex;gap:3px}
.dots i{width:7px;height:7px;border-radius:50%;background:#ddd}
.dots i.on{background:var(--green)}
.map{left:429px;top:126px;width:167px;height:171px;background:#fff;padding:3px}
.map .area{height:151px;background:linear-gradient(135deg,#e8efe0,#f4eedc 50%,#dfe9d5)}
.map .bar{height:14px;background:var(--green);color:#fff;font-size:8px;font-weight:700;padding:3px 4px;position:relative}

/* listings */
.listings{left:72px;top:317px;width:346px;height:618px;background:#fff}
.list-head{height:14px;background:var(--blue);color:#fff;font-size:10px;font-weight:700;padding:1px 8px}
.filters{height:20px;background:var(--band);color:#fff;font-size:7px;font-weight:700;margin-top:2px;position:relative}
.filters > span{position:absolute;top:6px;white-space:nowrap}
.filters .tri{color:var(--green)}
.venue{position:absolute;left:11px;width:324px;height:50px;background:#f7f7f7;border:1px solid #e5e5e5}
.venue.active{border-color:var(--green);background:#fff}
.thumb{position:absolute;left:8px;top:7px;width:36px;height:36px;background:linear-gradient(#e9f3f5,#7aa862 55%,#2e4d2a)}
.venue h3{position:absolute;left:58px;top:5px;font-size:10px;font-weight:700}
.venue .addr{position:absolute;left:58px;top:19px;font-size:7px;color:var(--muted)}
.venue .more{position:absolute;right:8px;top:5px;font-size:8px;font-weight:700}
.venue .save{position:absolute;right:8px;bottom:5px;font-size:7px;display:flex;align-items:center;gap:6px}
.venue .save i{width:8px;height:8px;border:1px solid #aaa;background:#fff}
.venue .actions{position:absolute;left:58px;bottom:6px;font-size:7px;display:flex;gap:10px}
.actions em{font-style:normal;color:var(--green-dark)}
.pager{position:absolute;right:10px;bottom:4px;font-size:8px;color:var(--orange)}
.pager span{color:#999}

/* sidebar */
.ad{left:429px;top:313px;width:167px;height:140px;background:radial-gradient(circle at 50% 55%,#cff27a,#5cb515 55%,#2c6f0a)}
.news{left:429px;top:457px;width:167px;height:88px;background:#fff;padding:2px 3px}
.news header{display:flex;justify-content:space-between;font-size:8px;padding:2px 1px 4px}
.news header a{color:var(--muted)}
.news li{list-style:none;height:13px;margin-bottom:1px;background:#999;color:#fff;font-size:8px;display:flex;justify-content:space-between;padding:2px 4px}
.news li b{font-weight:400}
.social-box{left:429px;top:556px;width:167px;height:128px;background:#fff;border:1px solid #c9d2e4;padding:4px}
.sb-head{display:flex;gap:4px;border-bottom:1px solid #dde;padding-bottom:4px}
.sb-head .sq{width:22px;height:22px;background:#3b5998}
.sb-head b{font-size:8px;color:#3b5998;display:block}
.sb-head span{display:inline-block;font-size:6px;border:1px solid #bbc;padding:0 3px;margin-top:3px}
.sb-count{font-size:6px;margin:4px 0}
.faces{display:flex;gap:4px}
.face{width:25px;text-align:center;font-size:5px}
.face i{display:block;height:22px;background:#b7a58d;margin-bottom:1px}
.sb-foot{font-size:5px;color:#3b5998;margin-top:4px}

/* newsletter */
.signup{left:72px;top:940px;width:346px;height:32px;background:#fff;padding:4px 10px}
.signup p{font-size:9px;width:110px;line-height:11px}
.signup p b{color:var(--green-dark);font-weight:400}
.signup .field{position:absolute;left:122px;top:8px;width:167px;height:18px;border:1px solid #ccc;font-size:7px;color:#999;padding:4px}
.signup .go{position:absolute;left:293px;top:8px;width:44px;height:18px;background:var(--orange);color:#fff;font-size:8px;text-align:center;line-height:18px}

/* footer */
.footer{left:72px;top:981px;width:524px;height:219px;background:var(--footer);color:var(--footer-text);font-size:7px}
.footer .icons{position:absolute;left:10px;top:8px;display:flex;gap:11px}
.footer .icons i{width:16px;height:16px;border-radius:50%;background:#e8e8e8}
.fcol{position:absolute;top:38px;line-height:11px;border-right:1px solid #333;height:108px}
.fcol h4{color:#ddd;font-size:9px;font-weight:400;margin-bottom:12px}
.fcol .sub{padding-left:10px}
.copy{position:absolute;left:102px;top:176px;line-height:11px}
.copy b{color:#ddd;font-weight:400}
</style>
</head>
<body>

<header class="abs topbar">
  <div class="brand">Pellora</div>
  <nav class="mainnav">
    <a class="current" href="#"><svg viewBox="0 0 12 12" fill="#fff"><path d="M6 1 0 6h2v5h3V8h2v3h3V6h2z"/></svg>Home</a>
    <a href="#"><svg viewBox="0 0 12 12" fill="#fff"><rect x="1" y="3" width="10" height="7" rx="1"/><rect x="4" y="1" width="4" height="2"/></svg>Events</a>
    <a href="#"><svg viewBox="0 0 12 12" fill="#fff"><path d="M6 0a4 4 0 0 0-4 4c0 3 4 8 4 8s4-5 4-8a4 4 0 0 0-4-4zm0 5.5A1.5 1.5 0 1 1 6 2.5a1.5 1.5 0 0 1 0 3z"/></svg>Venues</a>
    <a href="#"><svg viewBox="0 0 12 12" fill="#fff"><rect x="1" y="1" width="10" height="10"/><rect x="3" y="3" width="6" height="6" fill="#0aa6dc"/></svg>Cinema</a>
  </nav>
  <div class="search">Search...<svg viewBox="0 0 10 10" fill="none" stroke="#fff" stroke-width="1.5"><circle cx="4" cy="4" r="3"/><path d="M6 6l3 3"/></svg></div>
</header>

<div class="abs subbar">
  <span class="city" style="left:10px">City: <b>Roma ▾</b></span>
  <span style="left:122px">Add event<i class="plus">+</i></span>
  <span style="left:196px">Add venue<i class="plus">+</i></span>
  <span style="left:352px"><svg width="7" height="8" viewBox="0 0 7 8" fill="#fff"><rect x="0" y="3.5" width="7" height="4.5"/><path d="M1.5 3.5V2.5a2 2 0 0 1 4 0v1" fill="none" stroke="#fff"/></svg> Log in / Sign up</span>
  <span class="lang" style="left:478px">Eng ▾</span>
</div>

<section class="abs slider" role="img" aria-label="Glowing paper lanterns at a festival">
  <a class="arrow" style="left:0" href="#"><svg width="8" height="10" viewBox="0 0 8 10"><path d="M7 0 1 5l6 5z" fill="#fff"/></svg></a>
  <a class="arrow" style="right:0" href="#"><svg width="8" height="10" viewBox="0 0 8 10"><path d="M1 0l6 5-6 5z" fill="#fff"/></svg></a>
  <div class="caption"><h2>Good festival</h2><p>March 29</p></div>
  <div class="dots"><i class="on"></i><i></i><i></i><i></i><i></i></div>
</section>

<aside class="abs map">
  <div class="area" role="img" aria-label="Street map of Roma"></div>
  <div class="bar">View large Map<svg style="position:absolute;right:4px;top:2px" width="7" height="10" viewBox="0 0 12 16" fill="#fff"><path d="M6 0a6 6 0 0 0-6 6c0 4 6 10 6 10s6-6 6-10a6 6 0 0 0-6-6z"/></svg></div>
</aside>

<section class="abs listings">
  <div class="list-head">Venue listings</div>
  <div class="filters">
    <span style="left:10px"><b class="tri">◆</b>&nbsp; By category</span>
    <span style="left:90px"><b class="tri">◆</b>&nbsp; By distance</span>
    <span style="right:8px">Filter ▾</span>
  </div>

  <article class="venue" style="top:45px"><i class="thumb"></i><h3>National Museum</h3><p class="addr">Roma streets gym, museum</p><a class="more">View details&gt;&gt;</a><label class="save">Save venue<i></i></label></article>
  <article class="venue" style="top:101px"><i class="thumb"></i><h3>National Museum</h3><p class="addr">Roma streets gym, museum</p><a class="more">View details&gt;&gt;</a><label class="save">Save venue<i></i></label></article>
  <article class="venue" style="top:157px"><i class="thumb"></i><h3>National Museum</h3><p class="addr">Roma streets gym, museum</p><a class="more">View details&gt;&gt;</a><label class="save">Save venue<i></i></label></article>
  <article class="venue active" style="top:213px"><i class="thumb"></i><h3>National Museum</h3><p class="addr">Roma streets gym, museum</p><a class="more">View details&gt;&gt;</a><div class="actions"><span>Get directions &gt;</span><span>Share <em>■</em></span><span>View map <em>●</em></span></div><label class="save">Save venue<i></i></label></article>
  <article class="venue" style="top:269px"><i class="thumb"></i><h3>National Museum</h3><p class="addr">Roma streets gym, museum</p><a class="more">View details&gt;&gt;</a><label class="save">Save venue<i></i></label></article>
  <article class="venue" style="top:325px"><i class="thumb"></i><h3>National Museum</h3><p class="addr">Roma streets gym, museum</p><a class="more">View details&gt;&gt;</a><label class="save">Save venue<i></i></label></article>
  <article class="venue" style="top:381px"><i class="thumb"></i><h3>National Museum</h3><p class="addr">Roma streets gym, museum</p><a class="more">View details&gt;&gt;</a><label class="save">Save venue<i></i></label></article>
  <article class="venue" style="top:437px"><i class="thumb"></i><h3>National Museum</h3><p class="addr">Roma streets gym, museum</p><a class="more">View details&gt;&gt;</a><label class="save">Save venue<i></i></label></article>
  <article class="venue" style="top:493px"><i class="thumb"></i><h3>National Museum</h3><p class="addr">Roma streets gym, museum</p><a class="more">View details&gt;&gt;</a><label class="save">Save venue<i></i></label></article>
  <article class="venue active" style="top:549px"><i class="thumb"></i><h3>National Museum</h3><p class="addr">Roma streets gym, museum</p><a class="more">View details&gt;&gt;</a><div class="actions"><span>Get directions &gt;</span><span>Share <em>■</em></span><span>View map <em>●</em></span></div><label class="save">Save venue<i></i></label></article>

  <div class="pager">1 <span>|</span> 2 <span>|</span> 3 <span>|</span> 4 &nbsp;<span>Next</span> &nbsp;&nbsp; Saved items&gt;&gt;</div>
</section>

<aside class="abs ad" role="img" aria-label="Green advertisement for Brewlark beer"></aside>

<aside class="abs news">
  <header><span>Latest news</span><a>View all news &gt;&gt;</a></header>
  <ul>
    <li><b>Very good festival</b><span>March / 15</span></li>
    <li><b>Pictures from event</b><span>March / 05</span></li>
    <li><b>Family adventure</b><span>March / 09</span></li>
    <li><b>Hello morning</b><span>June / 04</span></li>
    <li><b>Seven days</b><span>April / 29</span></li>
  </ul>
</aside>

<aside class="abs social-box">
  <div class="sb-head"><i class="sq"></i><div><b>Socialnest Platform</b><span>Like</span></div></div>
  <p class="sb-count">4,622,220 people like <b>Socialnest Platform</b>.</p>
  <div class="faces">
    <div class="face"><i></i>Tomas</div><div class="face"><i></i>Lina</div><div class="face"><i></i>Orhan</div><div class="face"><i></i>Pavel</div><div class="face"><i></i>Nadia</div>
  </div>
  <div class="faces" style="margin-top:3px">
    <div class="face"><i style="height:14px"></i></div><div class="face"><i style="height:14px"></i></div><div class="face"><i style="height:14px"></i></div><div class="face"><i style="height:14px"></i></div><div class="face"><i style="height:14px"></i></div>
  </div>
  <p class="sb-foot">Socialnest social plugin</p>
</aside>

<section class="abs signup">
  <p>Receive weekly event list for <b>Roma</b></p>
  <div class="field">Enter your email here...</div>
  <div class="go">Sumbit</div>
</section>

<footer class="abs footer">
  <div class="icons"><i></i><i></i><i></i><i></i><i></i></div>
  <div class="fcol" style="left:22px;width:64px"><h4>Site pages</h4>Home<br>Events<br><span class="sub">Event Map</span><br>Venues<br>Cinema<br><span class="sub">Showtimes</span><br><span class="sub">Trailers</span><br>Blog / News</div>
  <div class="fcol" style="left:91px;width:72px"><h4>About Us</h4>About<br>Jobs<br>Advertise<br>Affiliate program<br>Contact Us</div>
  <div class="fcol" style="left:170px;width:70px"><h4>Your account</h4>Log in / Register<br>Add Event +<br>Add Venue +</div>
  <div class="fcol" style="left:251px;width:80px"><h4>Popular events</h4>Event1<br>Event2<br>Event3<br>Event4</div>
  <div class="fcol" style="left:339px;width:96px"><h4>Popular categories</h4>Terms of Use<br>Privacy policy<br>Send us feedback</div>
  <div class="fcol" style="left:441px;width:80px;border:0"><h4>Popular cinema</h4>Terms of Use<br>Terms of Use<br>Terms of Use</div>
  <p class="copy">Pellora Copyright © 2012 Q Ventures, LLC. All rights reserved.<br>Use of this website signifies your agreement to the <b>Terms of Use</b> and <b>Online Privacy Policy</b></p>
</footer>

</body>
</html>
```